Complete redesign of site for leading equipment supplier and service company

Looking for a new website design to portray our offerings for customers. Bay & Gate is a distributor, installer and service provider for loading dock equipment and industrial doors. We are a factory authorized dealer for a number of top brand names and also provide service after the sale on our equipment as well as competitors equipment. We are also in the midst of developing a service program tied to a QR coding system that would need to be incorporated in the website where a customer can scan a QR code and be brought to a specific "Service Request" portal that would be a form they could fill out to send to our service department.
Site should also feature product information pages for our base of product offerings, a completed projects area where we can showcase the work we've done, and a bio area for our sales and management team.

Some information for research:

Our Products That We Sell:

morrowliftworks.com
pallanraisetech.com
vqxgates.com
nhlsupplies.com
https://www.garvin-holtby.com/commercial-doors
https://www.pelmagates.com/
https://www.ulogates.com/

Similar Companies and Competitors:

http://www.quaddelmachinery.com/
https://www.easternbaysupplies.com/
https://www.moonmachinery.com/
https://www.ravenhollis.com/
https://pelvo.quandrift.com/en/us?gclid=ZqmPLRtyuv5XNCCFkpOmQD_ZYKJT0sVUr8PWHnm3K7Pxa3ZQ-PxluzkMnb-opiIIDmRtxu4BzJpTfLh9rmzDGbnwQ_ExcEB

Target Market(s)

Existing and potential customers throughout the greater New England region including:
Manufacturing
Distribution
Cold Storage
Pharmaceutical
Food Production
Beverage Bottling
Warehousing

Coding

Coded - Design and coding required

Number of Pages Required

5+ page

Colors
9ccb3b
ecf7fb

Requirements
Must have
• Home Page
Product Page
Service Page
Contact Page
Separate page that will be directed to from a QR code that we will supply to specific customers

```html
<!DOCTYPE html>
<html lang="en">
<head>
<meta charset="utf-8">
<title>Bay &amp; Gate — Loading Dock Equipment &amp; Industrial Doors</title>
<link rel="stylesheet" href="https://fonts.googleapis.com/css2?family=Montserrat:wght@500;600;700&family=Raleway:wght@400;500;600&display=swap">
<style>
:root{
  --green:#9ccb3b;
  --green-dark:#5e7f1e;
  --green-pale:#c9e59a;
  --ice:#ecf7fb;
  --ink:#2b2b2b;
  --text:#7a7a7a;
  --line:#d9d9d9;
  --footer:#2c2c2e;
  --white:#ffffff;
}
*{box-sizing:border-box;margin:0;padding:0}
html,body{width:1200px;height:4688px;overflow:hidden}
body{font-family:"Raleway",sans-serif;color:var(--ink);background:var(--white);position:relative}
h1,h2,h3{font-family:"Montserrat",sans-serif;font-weight:600}
.section-title{font-size:42px;text-align:center;color:var(--ink)}
.section-lead{font-size:14px;line-height:28px;color:var(--text);text-align:center;width:760px;margin:12px auto 0}
.btn{display:inline-block;font-family:"Raleway",sans-serif;font-size:15px;padding:0 24px;height:48px;line-height:48px;background:var(--green);color:#2a3a0c;box-shadow:5px 5px 0 var(--green-dark);text-decoration:none}
.btn--light{background:var(--ice);color:#2b3a44;box-shadow:5px 5px 0 var(--green)}
.abs{position:absolute}

/* Hero */
.hero{position:absolute;left:0;top:0;width:1200px;height:601px;overflow:hidden}
.hero__photo{position:absolute;inset:0;background:linear-gradient(180deg,#5d6470 0%,#4a5a86 30%,#3b4f85 55%,#5e6a78 80%,#7d8289 100%)}
.hero__shade{position:absolute;inset:0;background:rgba(20,30,60,.25)}
.brand-mark{position:absolute;left:110px;top:26px;display:flex;align-items:center;gap:10px;color:var(--white);font-family:"Montserrat",sans-serif;font-weight:600;font-size:18px}
.brand-mark i{display:block;width:22px;height:22px;background:var(--green)}
.topbar{position:absolute;right:113px;top:38px;display:flex;gap:30px;color:var(--white);font-size:15px}
.topbar span{display:flex;align-items:center;gap:10px}
.topbar svg{width:32px;height:32px}
.nav-rule{position:absolute;left:110px;right:110px;top:89px;border-top:1px solid rgba(255,255,255,.55)}
.nav{position:absolute;left:110px;right:110px;top:114px;display:flex;font-size:15px;color:var(--white)}
.nav a{color:var(--white);text-decoration:none;margin-right:53px}
.nav a.is-active{color:var(--green)}
.social{margin-left:auto;display:flex;gap:10px}
.social i{display:block;width:12px;height:12px;border:2px solid currentColor;border-radius:50%}
.hero__title{position:absolute;top:242px;width:100%;text-align:center;color:var(--white);font-size:50px;font-weight:600;letter-spacing:1px}
.hero__text{position:absolute;top:313px;left:300px;width:600px;text-align:center;color:var(--white);font-size:15px;line-height:32px}
.hero .btn{position:absolute;left:522px;top:396px;height:44px;line-height:44px;font-size:14px;padding:0 28px}
.slider-dots{position:absolute;top:556px;left:528px;display:flex;align-items:center;gap:14px;color:var(--white)}
.slider-dots i{display:block;width:12px;height:12px;border:1.5px solid var(--white);border-radius:50%}
.slider-dots i.on{background:var(--white)}

/* Services */
.services{position:absolute;top:690px;left:0;width:1200px}
.services__grid{display:flex;justify-content:center;gap:0;margin-top:30px}
.service{width:343px;text-align:center}
.service__icon{width:100px;height:100px;border:2px solid #c8c8c8;border-radius:50%;margin:0 auto;display:flex;align-items:center;justify-content:center}
.service__icon svg{width:54px;height:54px}
.service h3{font-family:"Raleway",sans-serif;font-weight:600;font-size:16px;margin-top:30px}
.service p{font-size:15px;line-height:28px;color:var(--text);margin-top:12px}

/* Featured */
.featured-band{position:absolute;top:1169px;left:0;width:1200px;height:515px;background:var(--green)}
.featured__head{position:absolute;top:1218px;width:1200px}
.featured__head .section-lead{color:#3c4a1c}
.arrow{position:absolute;width:20px;height:30px}
.product-card{position:absolute;top:1357px;width:317px;height:386px;box-shadow:0 2px 6px rgba(0,0,0,.25)}
.product-card p{position:absolute;left:12px;bottom:24px;right:12px;color:var(--white);font-size:14px;line-height:26px;font-weight:500}

/* Video */
.video{position:absolute;top:1923px;left:111px;width:976px;height:486px;background:linear-gradient(110deg,#3a3f47 0%,#3d424a 32%,#e2ac14 36%,#e6b41f 70%,#4b5059 74%,#9aa1a8 100%)}
.video__logo{position:absolute;left:40px;top:40px;width:72px;height:72px;background:#2d3134;border:2px solid var(--green);color:var(--white);font-family:"Montserrat",sans-serif;font-size:13px;font-weight:600;display:flex;align-items:center;justify-content:center;text-align:center;line-height:16px}
.video__play{position:absolute;left:444px;top:198px;width:86px;height:86px;border-radius:50%;background:#1f2122}
.video__caption{position:absolute;left:47px;top:420px;color:var(--white);font-size:19px;font-weight:500}
.video__bar{position:absolute;left:0;bottom:0;width:976px;height:27px;background:#3a3d40}

/* Solutions */
.solutions__title{position:absolute;left:111px;top:2508px;font-size:40px}
.solutions__text{position:absolute;left:111px;top:2576px;width:448px;font-size:15px;line-height:34.5px;color:var(--text);text-align:justify}
.solutions .btn{position:absolute;left:118px;top:2872px}
.solutions__frame{position:absolute;left:632px;top:2515px;width:455px;height:430px;background:linear-gradient(180deg,#b9bcbf 0%,#c9cbcd 45%,#8f9498 70%,#6d7175 100%)}
.solutions__frame::after{content:"";position:absolute;inset:14px;border:1.5px solid rgba(255,255,255,.85)}

/* Why */
.why{position:absolute;top:3047px;left:0;width:1200px;height:400px;background:linear-gradient(90deg,#1e2023 0%,#2f2a1c 40%,#3a3322 60%,#1e2023 100%)}
.why h2{position:absolute;top:56px;width:100%;text-align:center;color:var(--white);font-size:42px}
.why p{position:absolute;top:128px;left:122px;width:956px;text-align:center;color:var(--white);font-size:15px;line-height:33px}
.why .btn{position:absolute;top:282px;height:48px;line-height:48px;font-size:15px;padding:0 21px}

/* News */
.news__head{position:absolute;top:3538px;width:1200px}
.news-card{position:absolute;top:3673px;width:317px;height:484px;background:var(--white);box-shadow:0 1px 5px rgba(0,0,0,.18)}
.news-card__img{height:260px}
.news-card__body{padding:20px 12px 0}
.news-card__meta{font-size:14px;color:var(--text)}
.news-card__meta b{font-weight:500;color:var(--ink)}
.news-card h3{font-family:"Raleway",sans-serif;font-weight:500;font-size:15px;line-height:28px;margin-top:8px}
.news-card p{font-size:14px;line-height:28px;color:var(--text);margin-top:8px}
.news-card__more{display:flex;align-items:center;gap:8px;margin-top:14px;font-size:14px;color:var(--ink)}
.news-card__more::after{content:"";flex:1;border-top:1px solid var(--line);margin-right:12px}

/* Footer */
.footer{position:absolute;top:4261px;left:0;width:1200px;height:427px;background:var(--footer);color:var(--white)}
.footer__col{position:absolute;top:68px;font-size:15px}
.footer__col h4{font-weight:500;font-size:15px;padding-bottom:14px;display:inline-block}
.footer__col h4.ruled{border-bottom:1px solid #d5d5d5;padding-right:30px}
.footer__col ul{list-style:none;margin-top:20px}
.footer__col li{line-height:34px}
.footer__rule{position:absolute;left:111px;right:111px;top:306px;border-top:1px solid #9a9a9a}
.footer__brand{position:absolute;left:112px;top:339px;font-family:"Montserrat",sans-serif;font-weight:600;font-size:25px}
.footer__copy{position:absolute;left:112px;top:381px;font-size:15px}
.footer__social{position:absolute;right:111px;top:348px;display:flex;gap:10px}
.footer__social i{display:block;width:12px;height:12px;border:2px solid var(--white);border-radius:50%}
.footer__terms{position:absolute;right:111px;top:377px;font-size:15px}
</style>
</head>
<body>

<header class="hero">
  <div class="hero__photo" role="img" aria-label="Row of red loading dock doors on a blue warehouse wall"></div>
  <div class="hero__shade"></div>
  <div class="brand-mark"><i></i>Bay &amp; Gate</div>
  <div class="topbar">
    <span><svg viewBox="0 0 32 32"><circle cx="16" cy="16" r="14" fill="none" stroke="#fff" stroke-width="1.5"/><path d="M11 10l3 0 1 4-2 1c1 2 2 3 4 4l1-2 4 1v3c-6 1-12-5-11-11z" fill="none" stroke="#fff" stroke-width="1.3"/></svg>Call Now - 888-888-8888</span>
    <span><svg viewBox="0 0 32 32"><circle cx="16" cy="16" r="14" fill="none" stroke="#fff" stroke-width="1.5"/><circle cx="16" cy="13" r="4" fill="#fff"/><path d="M9 23c1-4 4-5 7-5s6 1 7 5z" fill="#fff"/></svg>Login</span>
  </div>
  <div class="nav-rule"></div>
  <nav class="nav">
    <a class="is-active">Home</a><a>About Us</a><a>Services</a><a>Products</a><a>Blog</a><a>Contact</a><a>ScanQR</a>
    <span class="social" aria-label="Social links"><i></i><i></i><i></i></span>
  </nav>
  <h1 class="hero__title">BAY &amp; GATE</h1>
  <p class="hero__text">Lorem ipsum dolor sit amet, consectetur adipiscing elit, sed do eiusmod tempor incididunt ut labore et dolore magna aliqua. Ut enim ad minim veniam,</p>
  <a class="btn">GET STARTED</a>
  <div class="slider-dots">
    <svg width="10" height="18"><path d="M9 1L1 9l8 8" fill="none" stroke="#fff" stroke-width="1.5"/></svg>
    <i></i><i class="on"></i><i></i><i></i>
    <svg width="10" height="18"><path d="M1 1l8 8-8 8" fill="none" stroke="#fff" stroke-width="1.5"/></svg>
  </div>
</header>

<section class="services">
  <h2 class="section-title">Our Services</h2>
  <p class="section-lead">Lorem ipsum dolor sit amet, consectetur adipiscing elit, sed do eiusmod tempor incididunt ut labore et dolore magna aliqua. Ut enim ad minim veniam,</p>
  <div class="services__grid">
    <div class="service">
      <div class="service__icon"><svg viewBox="0 0 54 54"><circle cx="27" cy="27" r="18" fill="none" stroke="#9ccb3b" stroke-width="3" stroke-dasharray="6 4"/><path d="M22 17a6 6 0 0 0 3 9l0 14h4V26a6 6 0 0 0 3-9v5h-3v-4h-4v4h-3z" fill="#7f8a8f"/></svg></div>
      <h3>Service &amp; repair</h3>
      <p>Lorem ipsum dolor sit amet, consectetur adipiscing elit, sed do eiusmod tempor incididunt ut labore et</p>
    </div>
    <div class="service">
      <div class="service__icon"><svg viewBox="0 0 54 54"><path d="M7 22L27 9l20 13v24H7z" fill="none" stroke="#7f8a8f" stroke-width="2.5"/><rect x="15" y="25" width="24" height="21" fill="#9ccb3b"/><path d="M15 30h24M15 35h24M15 40h24" stroke="#fff" stroke-width="1.5"/></svg></div>
      <h3>Modernisation &amp; upgradesVisa navigation</h3>
      <p>Lorem ipsum dolor sit amet, consectetur adipiscing elit, sed do eiusmod tempor incididunt ut labore et</p>
    </div>
    <div class="service">
      <div class="service__icon"><svg viewBox="0 0 54 54"><rect x="8" y="8" width="17" height="17" rx="3" fill="none" stroke="#7f8a8f" stroke-width="2.5"/><rect x="29" y="8" width="17" height="17" rx="3" fill="#9ccb3b"/><rect x="8" y="29" width="17" height="17" rx="3" fill="#9ccb3b"/><circle cx="37.5" cy="37.5" r="8" fill="none" stroke="#7f8a8f" stroke-width="2.5"/><circle cx="37.5" cy="37.5" r="2.5" fill="#7f8a8f"/></svg></div>
      <h3>E-maintenance</h3>
      <p>Lorem ipsum dolor sit amet, consectetur adipiscing elit, sed do eiusmod tempor incididunt ut labore et</p>
    </div>
  </div>
</section>

<div class="featured-band"></div>
<section class="featured">
  <div class="featured__head">
    <h2 class="section-title">Featured Products</h2>
    <p class="section-lead">Lorem ipsum dolor sit amet, consectetur adipiscing elit, sed do eiusmod tempor incididunt ut labore et dolore magna aliqua. Ut enim ad minim veniam,</p>
  </div>
  <svg class="arrow" style="left:80px;top:1350px" viewBox="0 0 20 30"><path d="M15 3L4 15l11 12" fill="none" stroke="#2b2b2b" stroke-width="2"/></svg>
  <svg class="arrow" style="left:1100px;top:1350px" viewBox="0 0 20 30"><path d="M5 3l11 12L5 27" fill="none" stroke="#fff" stroke-width="2"/></svg>
  <article class="product-card" style="left:111px;background:linear-gradient(180deg,#8e9296 0%,#a7abae 40%,#545a60 70%,#6b6f72 100%)" role="img" aria-label="Warehouse loading docks with grey doors">
    <p>Lorem ipsum dolor sit amet, consectetur adipiscing elit, sed do eiusmod</p>
  </article>
  <article class="product-card" style="left:441px;background:linear-gradient(160deg,#d67a4a 0%,#e8d8c6 30%,#c8ccd0 55%,#4a4b50 100%)" role="img" aria-label="White refrigerated truck at sunset">
    <p>Lorem ipsum dolor sit amet, consectetur adipiscing elit, sed do eiusmod</p>
  </article>
  <article class="product-card" style="left:770px;background:linear-gradient(100deg,#2a3d55 0%,#e0a817 30%,#e4b321 62%,#24384f 80%,#3c4048 100%)" role="img" aria-label="Yellow industrial sectional door on a blue building">
    <p>Lorem ipsum dolor sit amet, consectetur adipiscing elit, sed do eiusmod</p>
  </article>
</section>

<section class="how">
  <h2 class="section-title abs" style="top:1835px;width:1200px;font-size:48px;font-weight:500">How It Works</h2>
  <div class="video" role="img" aria-label="Video of a yellow industrial door at a warehouse">
    <div class="video__logo">Bay &amp;<br>Gate</div>
    <div class="video__play"><svg viewBox="0 0 86 86" width="86" height="86"><circle cx="43" cy="43" r="40" fill="none" stroke="#9ccb3b" stroke-width="2"/><path d="M37 34l14 9-14 9z" fill="#fff"/></svg></div>
    <div class="video__caption">Lorem ipsum dolor sit amet, consectetur adipiscing elit,</div>
    <div class="video__bar">
      <svg width="976" height="27" viewBox="0 0 976 27">
        <rect x="0" y="0" width="44" height="27" fill="#9ccb3b"/>
        <path d="M14 6l12 7.5L14 21z" fill="#fff"/>
        <rect x="44" y="0" width="550" height="27" fill="#9ccb3b"/>
        <rect x="594" y="0" width="215" height="27" fill="#c9e59a"/>
        <rect x="809" y="0" width="167" height="27" fill="#9ccb3b"/>
        <path d="M838 10h4l5-4v15l-5-4h-4z" fill="#fff"/>
        <circle cx="899" cy="13.5" r="6" fill="none" stroke="#fff" stroke-width="2"/>
        <path d="M940 7h6M940 7v6M966 20h-6M966 20v-6" stroke="#fff" stroke-width="2"/>
      </svg>
    </div>
  </div>
</section>

<section class="solutions">
  <h2 class="solutions__title">Solutions &amp; Applications</h2>
  <p class="solutions__text">Lorem ipsum dolor sit amet, consectetur adipiscing elit, sed do eiusmod tempor incididunt ut labore et dolore magna aliqua. Ut enim ad minim veniam, quis nostrud exercitation ullamco laboris nisi ut aliquip ex ea commodo consequat. Duis aute irure dolor in reprehenderit in voluptate velit esse cillum dolore eu fugiat nulla pariatur. Excepteur sint occaecat cupidatat non proident, sunt in culpa qui officia deserunt mollit anim id est laborum.</p>
  <a class="btn">READ MORE</a>
  <div class="solutions__frame" role="img" aria-label="White delivery trucks parked at numbered loading bays"></div>
</section>

<section class="why" role="img" aria-label="Dark warehouse facade with yellow doors at night">
  <h2>Why Bay &amp; Gate</h2>
  <p>Lorem ipsum dolor sit amet, consectetur adipiscing elit, sed do eiusmod tempor incididunt ut labore et dolore magna aliqua. Ut enim ad minim veniam, quis nostrud exercitation ullamco laboris nisi ut aliquip ex ea commodo consequat. Duis aute irure dolor in reprehenderit in voluptate velit esse cillum dolore eu fugiat nulla pariatur. Excepteur sint occaecat cupidatat non proident, sunt in culpa qui officia deserunt mollit anim id est laborum.</p>
  <a class="btn" style="left:402px">REQUEST A QUOTE</a>
  <a class="btn btn--light" style="left:606px">BECOME A PARTNER</a>
</section>

<section class="news">
  <div class="news__head">
    <h2 class="section-title">Latest News &amp; Articles</h2>
    <p class="section-lead" style="margin-top:8px">Lorem ipsum dolor sit amet, consectetur adipiscing elit, sed do eiusmod tempor incididunt ut labore et dolore magna aliqua. Ut enim ad minim veniam,</p>
  </div>
  <article class="news-card" style="left:111px">
    <div class="news-card__img" role="img" aria-label="Loading dock shelters against a blue wall" style="background:linear-gradient(180deg,#2a6fd0 0%,#3b7de0 35%,#aab0b6 55%,#8c9197 100%)"></div>
    <div class="news-card__body">
      <div class="news-card__meta"><b>June-20-20</b> - 10 comments</div>
      <h3>Nemo enim ipsam voluptatem quia voluptas sit aspernatur aut</h3>
      <p>Lorem ipsum dolor sit amet, &nbsp;elit, sed do eiusmod tempor incididunt ut</p>
      <div class="news-card__more">READ MORE</div>
    </div>
  </article>
  <article class="news-card" style="left:441px">
    <div class="news-card__img" role="img" aria-label="Red dock doors under a yellow facade" style="background:linear-gradient(180deg,#e8b316 0%,#e8b316 20%,#3a3c40 30%,#8e2a2a 50%,#5f6368 70%,#a6abb0 100%)"></div>
    <div class="news-card__body">
      <div class="news-card__meta"><b>June-20-20</b> - 10 comments</div>
      <h3>Nemo enim ipsam voluptatem quia voluptas sit aspernatur aut</h3>
      <p>Lorem ipsum dolor sit amet, &nbsp;elit, sed do eiusmod tempor incididunt ut</p>
      <div class="news-card__more">READ MORE</div>
    </div>
  </article>
  <article class="news-card" style="left:770px">
    <div class="news-card__img" role="img" aria-label="Warehouse building lit at dusk" style="background:linear-gradient(180deg,#1d2a40 0%,#24324a 40%,#3a3a36 70%,#1a1c20 100%)"></div>
    <div class="news-card__body">
      <div class="news-card__meta"><b>June-20-20</b> - 10 comments</div>
      <h3>Nemo enim ipsam voluptatem quia voluptas sit aspernatur aut</h3>
      <p>Lorem ipsum dolor sit amet, &nbsp;elit, sed do eiusmod tempor incididunt ut</p>
      <div class="news-card__more">READ MORE</div>
    </div>
  </article>
</section>

<footer class="footer">
  <div class="footer__col" style="left:111px">
    <h4>Contact us</h4>
    <ul style="margin-top:34px"><li>Email us - info@bayandgate.com</li><li>Call us - 888-888-8888</li></ul>
  </div>
  <div class="footer__col" style="left:386px">
    <h4 class="ruled">Support</h4>
    <ul><li>Help</li><li>Delivery</li><li>My Account</li><li>Faq</li><li>Contact</li></ul>
  </div>
  <div class="footer__col" style="left:572px">
    <h4>Buyer Guide</h4>
    <ul><li>Introduction</li><li>Searching</li><li>Payments</li><li>Shipping&amp;Pickup</li></ul>
  </div>
  <div class="footer__col" style="left:768px">
    <h4>Seller Guide</h4>
    <ul><li>Introduction</li><li>Payments Processing</li><li>Selling Materials</li><li>Sales Tax</li></ul>
  </div>
  <div class="footer__col" style="left:994px">
    <h4 class="ruled">Products</h4>
    <ul><li>Lorem ipsum</li><li>Lorem ipsum</li><li>Lorem ipsum</li><li>Lorem ipsum</li></ul>
  </div>
  <div class="footer__rule"></div>
  <div class="footer__brand">BAY &amp; GATE</div>
  <div class="footer__copy">copyrights©2020All Rights Reserved</div>
  <div class="footer__social" aria-label="Social links"><i></i><i></i><i></i></div>
  <div class="footer__terms">Terms &amp; Conditions</div>
</footer>

</body>
</html>
```